Labels for Transparent Egg Packs

We want to design a totally new label design concepts for my transparent egg packs , and I want the design in two sepearte sizes / dimensions.
We want it different from what we already have in the market , also using a diffrent color scheme. We want it bright and colorful , not crowded
• Label size 1 : 185*110mm
• Label size 2 : 70*190mm

Target Market(s)

Supermarkets and Retails outlets

Industry/Entity Type

Food

Colors
FFC000
F8CF3A
FAE287
FDF2CF
FEFAEE
F0912C
F2A743
F7CA91
FBE8D2
FDF5EE
EE7325
F08F49
F5BC92
FAE3D3
FDF4ED

Requirements
Must have
• See attached must haves , Must haves contents/ words in design: • Egg quantity: i.e.. 25 grade AA eggs, 30 grade AA eggs • Net weight • Fresh • Natural source of omega-3 • Contact information: __________________________________ Produced and Packaged by Tumbledew Farms Nigeria Address: 7c Morowale street , GRA , Ikeja ,Lagos, Nigeria Phone/ Whatsapp : +234 9017345620 , url:www. tumdew.food , Email : info@tumdew.food • Storage Condition : Store in a cool and dry Place • Recycle symbol: • BURTEM REG: • LKV stamp : • Barcode:
Nice to have
• See attached must haves
Should not have
• No need for Nutritional facts table

```html
<!DOCTYPE html>
<html lang="en">
<head>
<meta charset="utf-8">
<title>Tumdew Egg Pack Labels</title>
<link href="https://fonts.googleapis.com/css2?family=Montserrat:wght@400;500;600;700;800;900&display=swap" rel="stylesheet">
<style>
  :root{
    --orange:#F47A20;
    --orange-deep:#E5561C;
    --orange-faint:#F08F49;
    --orange-soft:#F5BC92;
    --green:#1D6B34;
    --white:#FFFFFF;
    --page:#FFFFFF;
  }
  *{box-sizing:border-box;margin:0;padding:0}
  html,body{width:1200px;height:1200px;overflow:hidden;background:var(--page)}
  body{position:relative;font-family:"Montserrat",sans-serif;color:var(--white)}
  .label{position:absolute;background:var(--orange);overflow:hidden}
  .label > *{position:absolute}
  .label svg.shape{left:0;top:0}
  .brand{font-weight:700;color:var(--white);letter-spacing:-1px;line-height:1;white-space:nowrap}
  .claims{list-style:none;font-weight:700;line-height:1.05}
  .claims li::before{content:"• "}
  .count{font-weight:900;line-height:1;color:var(--white);-webkit-text-stroke:10px var(--orange-deep);paint-order:stroke fill;letter-spacing:-4px}
  .grade{font-weight:800;white-space:nowrap}
  .illus-hen{background:var(--orange-deep);border-radius:40% 50% 30% 40%}
  .producer{font-weight:600;line-height:1.15}
  .contact{font-weight:700;line-height:1.15;white-space:nowrap}
  .contact .web,.contact .phone{font-size:16px}
  .contact .mail{font-size:12px;font-weight:500;padding-left:3px}
  .storage{font-weight:700;white-space:nowrap}
  .reg{font-weight:700;white-space:nowrap}
  .stamp-box{border:1.5px solid var(--white)}
  .recycle{width:26px;height:26px}

  /* size 1 */
  .label--25{left:48px;top:50px;width:525px;height:312px}
  .label--25 .brand{left:22px;top:28px;font-size:40px}
  .label--25 .net{left:242px;top:32px;font-size:11px;font-weight:700}
  .label--25 .claims{left:26px;top:95px;font-size:15px}
  .label--25 .count{left:160px;top:58px;font-size:146px}
  .label--25 .grade{left:156px;top:203px;font-size:21px}
  .label--25 .brand-faint{left:312px;top:46px;width:160px;font-size:40px;font-weight:700;color:var(--orange-faint);transform:rotate(-90deg);transform-origin:center;text-align:center}
  .label--25 .illus-hen{left:338px;top:168px;width:58px;height:56px}
  .label--25 .illus-leaves{left:18px;top:142px;width:120px;height:88px;background:var(--orange-faint);border-radius:60% 10% 60% 10%;opacity:.55}
  .label--25 .stamp-box.a{left:472px;top:160px;width:16px;height:62px}
  .label--25 .stamp-box.b{left:494px;top:160px;width:16px;height:62px}
  .label--25 .reg{font-size:10px;transform:rotate(-90deg);transform-origin:left top}
  .label--25 .reg.burtem{left:473px;top:307px}
  .label--25 .reg.lkv{left:495px;top:296px}
  .label--25 .producer{left:19px;top:238px;font-size:10.5px;color:var(--orange-soft);font-weight:500}
  .label--25 .recycle{left:183px;top:242px}
  .label--25 .contact{left:245px;top:240px}
  .label--25 .storage{left:19px;top:286px;font-size:11px}

  /* size 2 */
  .label--30{left:606px;top:847px;width:538px;height:198px}
  .label--30 .brand{left:79px;top:22px;font-size:40px}
  .label--30 .claims{left:80px;top:103px;font-size:14.5px}
  .label--30 .reg{font-size:9px}
  .label--30 .reg.burtem{left:80px;top:156px}
  .label--30 .reg.lkv{left:84px;top:174px}
  .label--30 .stamp-box.a{left:146px;top:152px;width:53px;height:15px}
  .label--30 .stamp-box.b{left:146px;top:170px;width:53px;height:15px}
  .label--30 .count{left:209px;top:58px;font-size:100px}
  .label--30 .grade{left:209px;top:158px;font-size:17px}
  .label--30 .producer{left:363px;top:10px;font-size:10.5px;font-weight:500}
  .label--30 .producer small{display:block;font-size:7px;margin-top:4px}
  .label--30 .illus-hen{left:360px;top:55px;width:58px;height:60px}
  .label--30 .recycle{left:426px;top:66px}
  .label--30 .storage{left:460px;top:67px;font-size:8.5px;line-height:1.15}
  .label--30 .net{left:423px;top:102px;font-size:9px;font-weight:700}
  .label--30 .contact{left:366px;top:133px}
</style>
</head>
<body>

<section class="label label--25" aria-label="Label for a pack of 25 eggs">
  <svg class="shape" width="525" height="312" viewBox="0 0 525 312" aria-hidden="true">
    <path d="M0 0H270C230 40 215 70 170 78C120 86 60 80 0 82Z" fill="var(--green)"/>
    <path d="M0 232C150 240 180 215 300 220C380 224 430 226 525 222V312H0Z" fill="var(--orange-deep)"/>
  </svg>
  <div class="illus-leaves" role="img" aria-label="Faint leaf decoration"></div>
  <div class="brand">tumdew</div>
  <div class="net">Net weight:</div>
  <ul class="claims"><li>Fresh</li><li>Natural source<br>&nbsp;&nbsp;of omega-3</li></ul>
  <div class="brand-faint">tumdew</div>
  <div class="count">25</div>
  <div class="grade">grade AA eggs</div>
  <div class="illus-hen" role="img" aria-label="Hen silhouette illustration"></div>
  <div class="stamp-box a"></div>
  <div class="stamp-box b"></div>
  <div class="reg burtem">BURTEM REG:</div>
  <div class="reg lkv">LKV STAMP:</div>
  <p class="producer">Produced and Packaged by<br>Tumbledew Farms Nigeria<br>7c Morowale Street, GRA, Ikeja<br>Lagos, Nigeria</p>
  <svg class="recycle" viewBox="0 0 24 24" aria-label="Recycle symbol" role="img">
    <g fill="none" stroke="var(--white)" stroke-width="2.2" stroke-linecap="round" stroke-linejoin="round">
      <path d="M8 9l3-5h2l2 3"/><path d="M13.5 7.5L15 7l.5-1.6"/>
      <path d="M17 11l3 5-1 2h-4"/><path d="M16.5 16.5L15 18l1.2 1.3"/>
      <path d="M10 19H5l-1-2 2-4"/><path d="M5 14.2L6 13l1.6.4"/>
    </g>
  </svg>
  <div class="contact">
    <div class="web">www.tumdew.food</div>
    <div class="mail">info@tumdew.food</div>
    <div class="phone">+234 9017345620</div>
  </div>
  <div class="storage">Store in a cool and dry Place</div>
</section>

<section class="label label--30" aria-label="Label for a pack of 30 eggs">
  <svg class="shape" width="538" height="198" viewBox="0 0 538 198" aria-hidden="true">
    <path d="M0 0H538V40C420 44 300 44 230 62C180 75 120 82 0 82Z" fill="var(--green)"/>
  </svg>
  <div class="brand">tumdew</div>
  <ul class="claims"><li>Fresh</li><li>Natural source<br>&nbsp;&nbsp;of omega-3</li></ul>
  <div class="reg burtem">BURTEM REG:</div>
  <div class="stamp-box a"></div>
  <div class="reg lkv">LKV STAMP:</div>
  <div class="stamp-box b"></div>
  <div class="count">30</div>
  <div class="grade">grade AA eggs</div>
  <p class="producer">Produced and Packaged by<br>Tumbledew Farms Nigeria<small>7c Morowale Street, GRA, Ikeja, Lagos, Nigeria</small></p>
  <div class="illus-hen" role="img" aria-label="Hen silhouette illustration"></div>
  <svg class="recycle" viewBox="0 0 24 24" aria-label="Recycle symbol" role="img">
    <g fill="none" stroke="var(--white)" stroke-width="2.2" stroke-linecap="round" stroke-linejoin="round">
      <path d="M8 9l3-5h2l2 3"/><path d="M13.5 7.5L15 7l.5-1.6"/>
      <path d="M17 11l3 5-1 2h-4"/><path d="M16.5 16.5L15 18l1.2 1.3"/>
      <path d="M10 19H5l-1-2 2-4"/><path d="M5 14.2L6 13l1.6.4"/>
    </g>
  </svg>
  <div class="storage">Store in a cool<br>and dry Place</div>
  <div class="net">Net weight:</div>
  <div class="contact">
    <div class="web">www.tumdew.food</div>
    <div class="mail">info@tumdew.food</div>
    <div class="phone">+234 9017345620</div>
  </div>
</section>

</body>
</html>
```